Atelier Mirou

I am actually making my own traditional french food.
Everything is homemade with passion.
I make differente terrines, jams, macaroons, rillettes and much more
I do as well cocktail party and catering

Hello everyone,

On the business card I would like to see appear if it's possible these following informations: traditional french food, cocktail party and catering.

```html
<!DOCTYPE html>
<html lang="en">
<head>
<meta charset="utf-8">
<title>Atelier Mirou – Business Card</title>
<link rel="stylesheet" href="https://fonts.googleapis.com/css2?family=Didact+Gothic&display=swap">
<style>
  :root {
    --page: #ffffff;
    --card-edge: #e81f2d;
    --card-mid: #a52a55;
    --card-core: #5a2e9c;
    --band: rgba(214, 24, 44, 0.85);
    --ink-dark: #231520;
    --ink-light: #ffffff;
    --role: #4b39b0;
    --outline: #3a1a22;
  }
  * { margin: 0; padding: 0; box-sizing: border-box; }
  html, body {
    width: 848px;
    height: 1200px;
    overflow: hidden;
    background: var(--page);
    font-family: "Didact Gothic", "Century Gothic", sans-serif;
  }
  .sheet {
    position: relative;
    width: 848px;
    height: 1200px;
  }
  .card {
    position: absolute;
    left: 150px;
    width: 555px;
    height: 308px;
    border-radius: 18px;
    border: 1px solid var(--outline);
    background: radial-gradient(ellipse 52% 62% at 50% 45%,
      var(--card-core) 0%, var(--card-mid) 55%, var(--card-edge) 100%);
    box-shadow: 0 14px 22px rgba(0, 0, 0, 0.28);
    overflow: hidden;
  }
  .card--front { top: 170px; }
  .card--back  { top: 685px; }

  .brand {
    position: absolute;
    top: 258px;
    left: 0;
    width: 100%;
    text-align: center;
    top: 84px;
  }
  .brand__dot {
    display: block;
    width: 22px;
    height: 22px;
    margin: 0 auto 14px;
    border-radius: 50%;
    background: var(--ink-dark);
  }
  .brand__name {
    font-size: 27px;
    letter-spacing: 1px;
    color: var(--ink-dark);
  }

  .services {
    position: absolute;
    left: 0;
    width: 100%;
    text-align: center;
    font-size: 13px;
    color: var(--ink-dark);
  }
  .card--front .services { top: 242px; }
  .card--back .services  { top: 18px; }

  .identity {
    position: absolute;
    top: 112px;
    left: 0;
    width: 100%;
    height: 68px;
    background: var(--band);
    text-align: center;
    padding-top: 11px;
  }
  .identity__name {
    font-size: 23px;
    color: var(--ink-light);
    line-height: 1.1;
  }
  .identity__role {
    font-size: 18px;
    color: var(--role);
    line-height: 1;
  }

  .contact {
    position: absolute;
    top: 212px;
    left: 200px;
    list-style: none;
    color: var(--ink-light);
    font-size: 20px;
  }
  .contact__item {
    display: flex;
    align-items: center;
    gap: 8px;
    height: 31px;
  }
  .contact__icon { width: 20px; height: 18px; flex: none; }
</style>
</head>
<body>
<main class="sheet">

  <section class="card card--front" aria-label="Card front">
    <div class="brand">
      <span class="brand__dot"></span>
      <p class="brand__name">Atelier Mirou</p>
    </div>
    <p class="services">Traditional french food • Cocktail party • Catering</p>
  </section>

  <section class="card card--back" aria-label="Card back">
    <p class="services">Traditional french food • Cocktail party • Catering</p>
    <div class="identity">
      <p class="identity__name">Julien Parmentier</p>
      <p class="identity__role">Owner</p>
    </div>
    <ul class="contact">
      <li class="contact__item">
        <svg class="contact__icon" viewBox="0 0 24 24" aria-hidden="true">
          <path fill="#2a1a22" d="M6.6 10.8a15.1 15.1 0 0 0 6.6 6.6l2.2-2.2c.3-.3.7-.4 1-.2 1.1.4 2.3.6 3.6.6.6 0 1 .4 1 1V20c0 .6-.4 1-1 1A17 17 0 0 1 3 4c0-.6.4-1 1-1h3.5c.6 0 1 .4 1 1 0 1.3.2 2.5.6 3.6.1.3 0 .7-.2 1z"/>
        </svg>
        <span>0455501234</span>
      </li>
      <li class="contact__item">
        <svg class="contact__icon" viewBox="0 0 24 18" aria-hidden="true">
          <rect x="1" y="1" width="22" height="16" fill="none" stroke="#2a1a22" stroke-width="2"/>
          <path d="M1 1l11 9 11-9" fill="none" stroke="#2a1a22" stroke-width="2"/>
        </svg>
        <span>julien.p@mirou.fr</span>
      </li>
    </ul>
  </section>

</main>
</body>
</html>
```